Business card for Industrial Automation Company.

The company is called Process and Motion Solutions. We are a systems integration company in South Africa specializing in PLC and SCADA programming, systems integration and industrial automation. Attached find logo and cover letter of the company for a feel of the general look. The website is still under development, so you will have to use your own ideas.

Please blend the colors on the business card as per the logo colors. Must be clean, professional look. Please submit a creative professional design. If a background color is used please do not use dark colored backgrounds.

Target Market(s)

Mining

Industry/Entity Type

Engineering Consultant

Contact Information for Business Card

Fanie du Plessis (NDip Electrical LC; BSc)
Director / Systems Engineer

Postal Address
PO Box 2836
Vredenburg
7380

Physical Address:
Bloubos Street 27
Vredenburg
7380

Tel: +22 548 6172
Cell: +27 82 395 4820
Mail: faniep@pms-za.example
Web: www.pms-za.example

Font styles to use
Sans Serif

Colors

Designer to choose colors to be used in the design.

Requirements
Must have
• Backside of the card must also contain the following:
• Services
• *Industrial Automation
• *Control System design and configuration
• *Systems Integration
• *Equipment Supply
• Industries
• *Mining
• *Factory
• *Oil and Gas
Nice to have
• Colors must blend in with colors of logo. Not too much color and no dark backgrounds.
Should not have
• dark / black background. Preferably white / light background if any.

```html
<!DOCTYPE html>
<html lang="en">
<head>
<meta charset="utf-8">
<title>Process and Motion Solutions – Business Card</title>
<link href="https://fonts.googleapis.com/css2?family=Open+Sans:wght@400;600;700&display=swap" rel="stylesheet">
<style>
  :root {
    --navy: #1d4a8f;
    --grey-text: #3c3c3c;
    --muted: #6b6b6b;
    --rule: #9fb2cf;
    --accent: #d8d72a;
    --card-white: #ffffff;
    --lavender: #8e95c8;
    --page: #e7e9ee;
  }
  * { box-sizing: border-box; margin: 0; padding: 0; }
  html, body { width: 1200px; height: 1200px; overflow: hidden; }
  body {
    background: var(--page);
    font-family: "Open Sans", Arial, sans-serif;
    color: var(--grey-text);
    position: relative;
  }
  .card {
    position: absolute;
    left: 240px;
    width: 720px;
    height: 400px;
    border-radius: 4px;
    box-shadow: 0 6px 18px rgba(0,0,0,.12);
    overflow: hidden;
  }
  .card--front { top: 130px; background: var(--card-white); }
  .card--back {
    top: 640px;
    background: radial-gradient(ellipse 75% 80% at 55% 35%, #ffffff 20%, #d9dbef 65%, var(--lavender) 115%);
  }

  /* brand lockup */
  .brand { position: absolute; display: flex; align-items: center; gap: 14px; }
  .brand__dot {
    width: 46px; height: 46px; border-radius: 50%;
    background: var(--navy);
    flex: none;
  }
  .brand__text { display: flex; flex-direction: column; }
  .brand__name {
    font-size: 24px; font-weight: 700; color: var(--navy);
    line-height: 1.1;
  }
  .brand__tagline {
    font-size: 13px; letter-spacing: 2px; color: var(--muted);
    margin-top: 4px;
  }
  .card--front .brand { top: 70px; left: 300px; }
  .card--back .brand { top: 80px; left: 50%; transform: translateX(-50%); white-space: nowrap; }

  /* front details */
  .contact { position: absolute; left: 48px; top: 175px; width: 630px; }
  .contact__name { font-size: 20px; color: var(--navy); text-transform: uppercase; letter-spacing: .3px; }
  .contact__name small { font-size: 14px; text-transform: none; color: var(--grey-text); letter-spacing: 0; }
  .contact__role { font-size: 14px; margin-top: 2px; }
  .contact__address { font-size: 14px; margin-top: 6px; }
  .label { color: var(--navy); }
  .contact__rule { height: 1px; background: var(--rule); margin: 10px 0 12px; }
  .contact__grid { display: flex; font-size: 14px; line-height: 1.7; }
  .contact__col { padding: 0 18px; border-left: 1px solid var(--rule); }
  .contact__col:first-child { padding-left: 0; border-left: 0; }
  .contact__line { display: flex; align-items: center; gap: 8px; }
  .icon { width: 14px; height: 14px; fill: var(--navy); flex: none; }

  /* back services */
  .services { position: absolute; top: 200px; left: 0; right: 0; text-align: center; }
  .services__title { font-size: 15px; letter-spacing: .5px; margin-bottom: 10px; }
  .services__line { font-size: 17px; line-height: 1.45; }
</style>
</head>
<body>

<section class="card card--front" aria-label="Card front">
  <div class="brand">
    <span class="brand__dot"></span>
    <div class="brand__text">
      <span class="brand__name">Process and Motion Solutions</span>
      <span class="brand__tagline">Engineering dependable control</span>
    </div>
  </div>

  <div class="contact">
    <p class="contact__name">Fanie du Plessis <small>(NDip Electrical LC; BSc)</small></p>
    <p class="contact__role">Director / Systems Engineer</p>
    <p class="contact__address"><span class="label">Physical Address</span> - Bloubos Street 27, Vredenburg, 7380</p>
    <div class="contact__rule"></div>
    <div class="contact__grid">
      <div class="contact__col">
        <p class="contact__line">
          <svg class="icon" viewBox="0 0 24 24"><path d="M6.6 10.8a15 15 0 0 0 6.6 6.6l2.2-2.2c.3-.3.7-.4 1-.2 1.1.4 2.3.6 3.6.6.6 0 1 .4 1 1V20c0 .6-.4 1-1 1A17 17 0 0 1 3 4c0-.6.4-1 1-1h3.5c.6 0 1 .4 1 1 0 1.3.2 2.5.6 3.6.1.3 0 .7-.2 1z"/></svg>
          +22 548 6172
        </p>
        <p class="contact__line">
          <svg class="icon" viewBox="0 0 24 24"><path d="M7 1h10a2 2 0 0 1 2 2v18a2 2 0 0 1-2 2H7a2 2 0 0 1-2-2V3a2 2 0 0 1 2-2zm0 3v14h10V4zm5 15.5a1.2 1.2 0 1 0 0 2.4 1.2 1.2 0 0 0 0-2.4z"/></svg>
          +27 82 395 4820
        </p>
      </div>
      <div class="contact__col">
        <p class="contact__line">
          <svg class="icon" viewBox="0 0 24 24"><path d="M12 2a10 10 0 1 0 0 20 10 10 0 0 0 0-20zm0 2c.9 0 2.3 1.8 2.9 5H9.1C9.7 5.8 11.1 4 12 4zM4.3 11h3.8c0 .7 0 1.3.1 2H4.3a8 8 0 0 1 0-2zm.6 4h3.5c.3 1.6.8 3 1.4 4A8 8 0 0 1 4.9 15zm3.5-6H4.9a8 8 0 0 1 4.9-4c-.6 1-1.1 2.4-1.4 4zM12 20c-.9 0-2.3-1.8-2.9-5h5.8c-.6 3.2-2 5-2.9 5zm3.1-7H8.9a16 16 0 0 1 0-2h6.2a16 16 0 0 1 0 2zm-.9 6c.6-1 1.1-2.4 1.4-4h3.5a8 8 0 0 1-4.9 4zm1.7-6c.1-.7.1-1.3.1-2h3.8a8 8 0 0 1 0 2zm-.3-4c-.3-1.6-.8-3-1.4-4a8 8 0 0 1 4.9 4z"/></svg>
          www.pms-za.example
        </p>
        <p class="contact__line">
          <svg class="icon" viewBox="0 0 24 24"><path d="M2 5h20v14H2zm2 2v.4l8 5.2 8-5.2V7zm0 2.8V17h16V9.8l-8 5.2z"/></svg>
          faniep@pms-za.example
        </p>
      </div>
      <div class="contact__col">
        <p class="label">Postal Address</p>
        <p>PO Box 2836, Vredenburg, 7380</p>
      </div>
    </div>
  </div>
</section>

<section class="card card--back" aria-label="Card back">
  <div class="brand">
    <span class="brand__dot"></span>
    <div class="brand__text">
      <span class="brand__name">Process and Motion Solutions</span>
      <span class="brand__tagline">Engineering dependable control</span>
    </div>
  </div>

  <div class="services">
    <p class="services__title">SERVICES</p>
    <p class="services__line">Industrial Automation | Control System design and configuration</p>
    <p class="services__line">Systems Integration | Equipment Supply | PLC and SCADA</p>
    <p class="services__line">Mining | Factory | Oil and Gas</p>
  </div>
</section>

</body>
</html>
```